Halt and Thicken New Branding Stationary Set - updated Oct 30th 2017

Updated on 30th Oct 2017 as we now need a whole folder design instead of a folder cover. We have thought out exactly what should be on it so it wont be hard. We are happy for this to be completed only by the winning designer if you like. And also we are guaranteeing this project now. Thanks!

We just got our new logo and now we would like a stationary set so we can brand our company communications. The items we need designed are:
Business cards
Letterhead
Appointment confirmation cards
Folder - switched from folder cover. Note that if you don't wish to do this unless you are selected as the winner this is fine.

1. Business cards - for 5 employees, final names will be given once the winner is selected, but you can use this one as the sample:
Lucinda Prieto
Hair Regrowth Expert
Halt and Thicken
7127 Marbury Ave, Suite 500
Kestrel Park CA 90877
lucinda@gavinthorpemd.example
(555) 238-9016

2. Letterhead 8.5" x 11.0" vertical
Halt and Thicken
Kestrel Park CA 90877
office@haltandthicken.example
(555) 238-9016

3. Appointment Confirmation cards - business card size
Halt and Thicken
Kestrel Park CA 90877
Appointment For:
Date:
Time:
If you are unable to make your appointment, please contact us to reschedule at:
(555) 238-9016
info@gavinthorpemd.example

*UPDATED*
4. Folder 9" x 12 " vertical with double pocket
We would like the infinity image from the logo made really big so the left side is on the back and the right side with the + sign is on the front and its takes up the maximum room on the folder.
On the front below the half logo it should say "A Biochemical Revolution..."
On the inside we would also like to have the infinity sign from the logo but faded and half on the left pocket half on the right.
On left inside pocket it should say (this will be partically written on top of the logo):
Gavin Thorpe MD
Precision Medicine
Halt and Thicken Hair
On the Right inside pocket it should say the following:
Because the Enemy of BETTER Health is Good Health
BETTER Ingredients
BETTER Recipe
BETTER Medicine
On the back below the logo on the bottom should be the contact information.
I attached a picture of our drawing of what we want for this to make it easier.

Here is our website to give you an idea of our branding: http://www.haltandthicken.example/

We are the only true cure for hair loss and need to look professional and highest quality and beyond reproach from an ethical standpoint. We are a medical clinic so this should be portrayed also.
We cured hair loss by analyzing biochemistry and rebalancing it so that the process reverses and your own hair can grow back naturally.

Business card information:

OK so here is the information for the business cards:

Lucinda Prieto
Hair Regrowth Expert
(555) 238-9016
www.haltandthicken.example

Marisol Quintero
Hair Growth Consultant
(555) 238-9016
marisol@gavinthorpemd.example
www.haltandthicken.example

Glenda Hutchins
CMO/COO
(555) 238-9016
glenda@haltandthicken.example
www.haltandthicken.example

Dr Lou Thorpe
President
(555) 238-9016
info@gavinthorpemd.example
www.haltandthicken.example

Halt and Thicken
Customer Service
(555) 238-9016
info@gavinthorpemd.example
www.haltandthicken.example

Target Market(s)

Men aged 20-24 who care about their appearance, care about their hair and care about the world.

Industry/Entity Type

Medical And Science

Font styles to use
Sans Serif

Colors
00a990
ffffff
9d9d9d
333333

Requirements
Must have
• Must use the logo and our brand colors from the logo in all designs.
• The pantone colors are:
• Green: #4ca26f
• Light Grey: #999999
• The design should be symmetrical and balanced.
Nice to have
• It should look reasonably masculine.
Should not have
• Do not include any red in the design.

```html
<!DOCTYPE html>
<html lang="en">
<head>
<meta charset="utf-8">
<title>Halt and Thicken — Stationery Set</title>
<link href="https://fonts.googleapis.com/css2?family=Roboto:wght@300;400;500&family=Roboto+Condensed:wght@700&family=Yellowtail&display=swap" rel="stylesheet">
<style>
  :root{
    --green:#4ca26f;
    --grey:#999999;
    --ink:#333333;
    --paper:#ffffff;
    --stage:#555555;
    --rule:#bdbdbd;
  }
  *{box-sizing:border-box;margin:0;padding:0}
  html,body{width:1200px;height:900px;overflow:hidden}
  body{background:var(--stage);font-family:'Roboto',Arial,sans-serif;color:var(--ink);position:relative;-webkit-font-smoothing:antialiased;-moz-osx-font-smoothing:grayscale}
  .sheet{position:absolute;background:var(--paper);overflow:hidden}

  /* brand lockup */
  .brand{position:absolute;display:flex;flex-direction:column;align-items:center;gap:5px}
  .brand-dot{width:18px;height:18px;border-radius:50%;background:var(--green)}
  .brand-name{font-family:'Roboto',Arial,sans-serif;font-weight:500;color:var(--green);letter-spacing:.2px;white-space:nowrap}

  /* letterhead */
  .letterhead{left:80px;top:76px;width:454px;height:586px}
  .letterhead .brand{left:38px;top:34px}
  .letterhead .brand-name{font-size:14px}
  .lh-contact{position:absolute;left:290px;top:47px;border-left:1px solid var(--rule);padding-left:8px;font-size:6.6px;font-weight:300;color:#777;line-height:9px}
  .lh-contact .gap{height:5px}
  .ico{display:inline-block;width:6px;height:6px;border-radius:50%;background:var(--green);margin-right:3px;vertical-align:-1px}
  .recipient{position:absolute;left:38px;top:174px;font-size:7.4px;line-height:9px;color:var(--ink)}
  .recipient b{font-weight:500;font-size:8.4px;display:block;margin-bottom:4px}
  .letter-body{position:absolute;left:38px;top:238px;width:380px;font-size:7.8px;line-height:13.4px;letter-spacing:-.1px;text-align:left;color:var(--ink);font-weight:400}
  .letter-body p+p{margin-top:13px}
  .signoff{position:absolute;left:38px;top:414px;font-size:7.4px;color:var(--ink)}
  .signature{position:absolute;left:37px;top:428px;font-family:'Yellowtail',cursive;font-size:28px;line-height:34px;color:var(--ink)}
  .signer{position:absolute;left:38px;top:472px;font-size:7.6px;line-height:10px;color:var(--ink)}
  .sheet-foot{position:absolute;left:0;right:0;display:flex;align-items:center;gap:6px}
  .sheet-foot .line{flex:1;height:1px;background:var(--rule)}
  .sheet-foot .url{color:var(--green);font-size:6.6px;letter-spacing:.2px}
  .letterhead .sheet-foot{top:554px}
  .letterhead .sheet-foot .line:last-child{flex:0 0 36px}
  .band{position:absolute;left:0;right:0;background:var(--green)}
  .letterhead .band{top:568px;height:12px}

  /* folder */
  .folder{left:632px;top:77px;width:456px;height:585px}
  .folder .brand{left:36px;top:28px}
  .folder .brand-name{font-size:13px}
  .folder .top-rule{position:absolute;left:0;right:0;top:122px;height:4px;background:var(--green)}
  .photo{position:absolute}
  .ph-consult{left:0;top:126px;width:193px;height:148px;background:linear-gradient(135deg,#c9d9cf,#5aa7a2 60%,#8e8475)}
  .ph-portrait{left:0;top:275px;width:193px;height:240px;background:linear-gradient(160deg,#d9cbb9,#8c6f58 55%,#4a3b31)}
  .ph-medical{left:194px;top:126px;width:262px;height:268px;background:linear-gradient(135deg,#eef4f8,#c7dbe8 55%,#3f6e96)}
  .ph-scalp{left:194px;top:395px;width:137px;height:120px;background:linear-gradient(135deg,#b9a28b,#7c6552 60%,#e7e2dc)}
  .ph-exam{left:332px;top:395px;width:124px;height:120px;background:linear-gradient(135deg,#e3d9d0,#a08c7c 55%,#3a3a3a)}
  .awareness{position:absolute;left:12px;top:443px;font-family:'Roboto Condensed','Arial Narrow',sans-serif;font-weight:700;font-size:14px;line-height:17.5px;color:#fff}
  .folder .band{top:515px;height:10px}
  .folder-url{position:absolute;left:0;right:0;top:556px;text-align:center;font-size:7.4px;letter-spacing:1px;color:var(--ink)}
  .folder-url span{color:var(--green)}

  /* cards */
  .card{top:704px;height:126px}
  .card-brand{left:80px;width:220px}
  .card-brand .brand{left:0;right:0;top:34px}
  .card-brand .brand-name{font-size:12px}
  .card .sheet-foot{top:107px;padding:0 4px}
  .card .sheet-foot .url{font-size:5.6px}
  .card .band{top:116px;height:5px}

  .card-appt{left:315px;width:221px}
  .appt-title{position:absolute;left:0;right:0;top:13px;text-align:center;font-weight:500;font-size:12px;color:var(--green)}
  .appt-rule{position:absolute;left:17px;right:17px;top:45px;height:1px;background:var(--rule)}
  .appt-head{position:absolute;left:0;right:0;top:51px;text-align:center;font-size:8px;color:var(--green)}
  .days{position:absolute;left:16px;right:14px;top:68px;display:flex;justify-content:space-between;font-size:4.6px;color:#777}
  .days span{display:flex;align-items:flex-end;gap:4px}
  .days i{display:block;width:7px;height:7px;border:1px solid #999}
  .when{position:absolute;left:16px;right:14px;top:84px;display:flex;align-items:flex-end;gap:6px;font-size:5.4px;color:#777}
  .when .fill{flex:1;height:1px;background:#999;margin-bottom:1px}
  .when .ampm{line-height:5px;text-align:right}
  .appt-foot{position:absolute;left:0;right:0;top:108px;height:18px;background:var(--green);color:#fff;font-size:4.6px;line-height:5.6px;text-align:center;padding-top:3px}

  .card-green{left:633px;width:223px;background:var(--green);border-radius:6px}
  .card-green .brand{left:0;right:0;top:38px}
  .card-green .brand-dot{background:#fff}
  .card-green .brand-name{color:#fff;font-size:12px}

  .card-person{left:865px;width:223px;border-radius:6px}
  .card-person .brand{left:10px;top:42px}
  .card-person .brand-dot{width:14px;height:14px}
  .card-person .brand-name{font-size:8.6px}
  .person{position:absolute;left:113px;top:34px;border-left:1px solid var(--rule);padding-left:5px;font-size:4.9px;color:#888;line-height:6.4px;font-weight:300}
  .person b{display:block;font-weight:400;font-size:7.6px;color:var(--ink);line-height:8px}
  .person .role{color:var(--green);margin-bottom:4px}
  .person .gap{height:3px}
</style>
</head>
<body>

<!-- Letterhead -->
<section class="sheet letterhead">
  <div class="brand"><div class="brand-dot"></div><div class="brand-name">HALT AND THICKEN</div></div>
  <div class="lh-contact">
    <div>7127 Marbury Ave, Suite 500</div>
    <div>Kestrel Park CA 90877</div>
    <div class="gap"></div>
    <div><span class="ico"></span>(555) 238-9016</div>
    <div><span class="ico"></span>lucinda@gavinthorpemd.example</div>
  </div>
  <div class="recipient"><b>JOHN SMITH</b>Street Name,City Name.<br>Zip Coad 0000</div>
  <div class="letter-body">
    <p>Lorem Ipsum is simply dummy text of the printing and typesetting industry. Lorem Ipsum has been the industry's standard dummy text ever since the 1500s, when an unknown printer took a galley of type and scrambled it to make a type specimen book. It has survived not only five centuries,but also the leap into electronic typesetting, remaining essentially unchanged. It was popularised in the 1960s with the release of Letraset sheets containing Lorem Ipsum passages, and more recently with desktop publishing software like Aldus PageMaker including versions of Lorem Ipsum.</p>
    <p>It is a long established fact that a reader will be distracted by the readable content of a page when looking at its layout. The point of using Lorem Ipsum is that it has a more-or-less normal distribution of letters, as opposed to using 'Content here, content here', making it look like readable English. Many desktop and over the years, sometimes by accident, sometimes on purpose (injected humour and the like).</p>
  </div>
  <div class="signoff">Regards,</div>
  <div class="signature">John Doe</div>
  <div class="signer">John Doe<br>General Maneger</div>
  <div class="sheet-foot"><div class="line"></div><div class="url">www.haltandthicken.example</div><div class="line"></div></div>
  <div class="band"></div>
</section>

<!-- Folder -->
<section class="sheet folder">
  <div class="brand"><div class="brand-dot"></div><div class="brand-name">HALT AND THICKEN</div></div>
  <div class="top-rule"></div>
  <div class="photo ph-consult" role="img" aria-label="Photo of a clinician examining a client's scalp in the clinic"></div>
  <div class="photo ph-portrait" role="img" aria-label="Close-up portrait photo of a young man with a full head of hair"></div>
  <div class="photo ph-medical" role="img" aria-label="Photo of a doctor with stethoscope and a hexagon medical icon overlay in blue"></div>
  <div class="photo ph-scalp" role="img" aria-label="Photo of a gloved hand giving a scalp treatment injection"></div>
  <div class="photo ph-exam" role="img" aria-label="Photo of a scalp being examined with a dermatoscope"></div>
  <div class="awareness">August:<br>National Hair Loss<br>Awareness Month</div>
  <div class="band"></div>
  <div class="folder-url">www.<span>HALTANDTHICKEN</span>.example</div>
</section>

<!-- Business card front -->
<section class="sheet card card-brand">
  <div class="brand"><div class="brand-dot"></div><div class="brand-name">HALT AND THICKEN</div></div>
  <div class="sheet-foot"><div class="line"></div><div class="url">www.haltandthicken.example</div><div class="line"></div></div>
  <div class="band"></div>
</section>

<!-- Appointment card -->
<section class="sheet card card-appt">
  <div class="appt-title">HALT AND THICKEN</div>
  <div class="appt-rule"></div>
  <div class="appt-head">Has An Appointment On</div>
  <div class="days">
    <span><i></i>Mon</span><span><i></i>Tues</span><span><i></i>Wed</span><span><i></i>Thur</span><span><i></i>Fri</span><span><i></i>Sat</span>
  </div>
  <div class="when"><span>Date</span><div class="fill"></div><span>AT</span><div class="fill"></div><span class="ampm">am.<br>pm.</span></div>
  <div class="appt-foot">If you are unable to make your appointment, please contact us to reschedule at:<br>P: (555) 238-9016 | E: info@gavinthorpemd.example</div>
</section>

<!-- Green card -->
<section class="sheet card card-green">
  <div class="brand"><div class="brand-dot"></div><div class="brand-name">HALT AND THICKEN</div></div>
</section>

<!-- Personal card -->
<section class="sheet card card-person">
  <div class="brand"><div class="brand-dot"></div><div class="brand-name">HALT AND THICKEN</div></div>
  <div class="person">
    <b>Lucinda Prieto</b>
    <div class="role">Hair Regrowth Expert</div>
    <div>7127 Marbury Ave, Suite 500</div>
    <div>Kestrel Park CA 90877</div>
    <div class="gap"></div>
    <div><span class="ico"></span>(555) 238-9016</div>
    <div><span class="ico"></span>lucinda@gavinthorpemd.example</div>
  </div>
  <div class="sheet-foot"><div class="line"></div><div class="url">www.haltandthicken.example</div><div class="line"></div></div>
  <div class="band"></div>
</section>

</body>
</html>
```